Business Card Design Project

I am community manager and social media strategist. I need a double sided business card with company logo and name. Looking for something professional, elegant but also a little bit original.

• - The logo and the colours are the company colours and a required to stay.
- The size should be: 84 x 55 mm (or 3.30 x 2.16)
- The file size should be: 1039 x 697 pixels (300 dpi)
- I'd like rounded corners. :)

Use the following contact information for the card:

Léonie Vardin
Stratégie médias sociaux / community management / édition de sites sociaux
mob. : 0687529103
leonie.vardin@postelune.fr
Chirp. : @lvardin
Vocall : vardin.leonie

```html
<!DOCTYPE html>
<html lang="fr">
<head>
<meta charset="UTF-8">
<title>Orvane – Léonie Vardin, carte de visite</title>
<link rel="stylesheet" href="https://fonts.googleapis.com/css2?family=Caladea:wght@400;700&display=swap">
<style>
  :root {
    --page-bg: #ffffff;
    --card-front-bg: #ffffff;
    --card-edge: #b9b9b9;
    --brand-blue: #2b5b99;
    --brand-mark: #3b72b3;
    --back-deep: #2a5690;
    --back-mid: #3566a3;
    --back-light: #4a7db8;
    --back-text: #ffffff;
    --divider: rgba(255, 255, 255, 0.85);
  }
  * { margin: 0; padding: 0; box-sizing: border-box; }
  html, body {
    width: 1200px;
    height: 900px;
    overflow: hidden;
    background: var(--page-bg);
  }
  .canvas {
    position: relative;
    width: 1200px;
    height: 900px;
    font-family: "Caladea", Cambria, Georgia, serif;
  }
  .card {
    position: absolute;
    left: 270px;
    width: 636px;
    height: 416px;
    border-radius: 42px;
    overflow: hidden;
  }
  .card-front {
    top: 36px;
    background: var(--card-front-bg);
    border: 1.5px solid var(--card-edge);
    z-index: 1;
  }
  .brand {
    position: absolute;
    left: 0;
    right: 0;
    top: 106px;
    display: flex;
    flex-direction: column;
    align-items: center;
  }
  .brand-dot {
    width: 128px;
    height: 128px;
    border-radius: 50%;
    background: var(--brand-mark);
  }
  .brand-name {
    margin-top: 18px;
    font-size: 62px;
    font-weight: 700;
    letter-spacing: 3px;
    line-height: 1;
    color: var(--brand-blue);
  }
  .card-back {
    top: 452px;
    z-index: 2;
    color: var(--back-text);
    text-align: center;
  }
  .back-wash {
    position: absolute;
    inset: 0;
    background: linear-gradient(115deg, var(--back-deep) 0%, var(--back-mid) 50%, var(--back-light) 100%);
  }
  .holder-name {
    position: absolute;
    top: 142px;
    left: 0;
    right: 0;
    font-size: 28px;
    font-weight: 400;
    line-height: 1;
  }
  .services {
    position: absolute;
    top: 198px;
    left: 0;
    right: 0;
    display: flex;
    justify-content: center;
    align-items: center;
    font-size: 17.5px;
    line-height: 1;
  }
  .service + .service {
    border-left: 1.5px solid var(--divider);
    margin-left: 6px;
    padding-left: 6px;
  }
  .contact-list {
    position: absolute;
    top: 246px;
    left: 0;
    right: 0;
    list-style: none;
    font-size: 19px;
    line-height: 24px;
  }
</style>
</head>
<body>
<main class="canvas">
  <section class="card card-front" aria-label="Recto">
    <div class="brand">
      <span class="brand-dot" aria-hidden="true"></span>
      <span class="brand-name">ORVANE</span>
    </div>
  </section>

  <section class="card card-back" aria-label="Verso">
    <div class="back-wash" role="img" aria-label="Fond bleu à vagues douces"></div>
    <h1 class="holder-name">Léonie Vardin</h1>
    <p class="services">
      <span class="service">Stratégie Médias Sociaux</span>
      <span class="service">Community Management</span>
      <span class="service">Édition De Sites Sociaux</span>
    </p>
    <ul class="contact-list">
      <li>Mob. : 0687529103</li>
      <li>leonie.vardin@postelune.fr</li>
      <li>Chirp. : @lvardin</li>
      <li>Vocall : vardin.leonie</li>
    </ul>
  </section>
</main>
</body>
</html>
```